Business card design for IT consulting company

Looking for a simple, modern, clean business card design.
Open to reworking our existing logo.

Attached is our current business cards which we do not like.
Ideally double sided with something simple on the back.
Rectangle / Horizonal only.
No rounded edges on the card.
White as the dominate color is preferred.

Target Market(s)

clients, legal, oil & gas, medical, professionals

Industry/Entity Type

IT, tech, consulting

Contact Information for Business Card

Name, Title, email, phone, cell, website

Font styles to use
Sans Serif

Requirements
Must have
• Clean design
Should not have
• loud colors or unusual fonts, etc

```html
<!DOCTYPE html>
<html lang="en">
<head>
<meta charset="utf-8">
<title>Norvane Solutions — Business Card</title>
<link href="https://fonts.googleapis.com/css2?family=Arimo:ital,wght@0,400;0,700;1,400&display=swap" rel="stylesheet">
<style>
  :root {
    --backdrop: #4b4b4d;
    --card-white: #f7f7f7;
    --card-grey: #5c5c5e;
    --edge-blue: #1b86c8;
    --ink: #1d1d1f;
    --ink-soft: #3a3a3c;
    --divider: #c9c9c9;
    --accent-yellow: #e8b422;
    --accent-red: #d83a4f;
    --accent-sky: #3bb1e3;
    --accent-navy: #2a2a7a;
  }
  * { box-sizing: border-box; margin: 0; padding: 0; }
  html, body {
    width: 1200px; height: 1108px; overflow: hidden;
    background: var(--backdrop);
    font-family: "Arimo", Arial, sans-serif;
    color: var(--ink);
  }
  .stage {
    position: relative; width: 1200px; height: 1108px;
    display: flex; flex-direction: column; align-items: center; justify-content: center; gap: 64px;
  }
  .card {
    width: 740px; height: 423px;
    border-bottom: 4px solid var(--edge-blue);
    box-shadow: 0 18px 40px rgba(0,0,0,.35);
    position: relative;
  }
  .card--front { background: var(--card-white); display: flex; align-items: center; }
  .card--back { background: var(--card-grey); display: flex; align-items: center; justify-content: center; }

  .brand { display: flex; align-items: center; gap: 14px; }
  .brand__square { width: 62px; height: 62px; background: var(--accent-navy); border-radius: 6px; }
  .brand__name { font-weight: 700; font-size: 30px; letter-spacing: .3px; color: var(--ink); }

  .card--front .brand { width: 400px; justify-content: center; padding-left: 20px; }
  .divider { width: 1px; height: 190px; background: var(--divider); }

  .contact { padding-left: 40px; }
  .contact__name { font-weight: 700; font-size: 22px; letter-spacing: .5px; }
  .contact__title { font-style: italic; font-size: 14px; color: var(--ink-soft); margin-top: 2px; margin-bottom: 18px; }
  .contact__list { list-style: none; }
  .contact__item { display: flex; align-items: center; gap: 12px; font-size: 15px; line-height: 23px; color: var(--ink-soft); letter-spacing: .4px; }
  .contact__icon { width: 14px; height: 14px; flex: none; }

  .card--back .brand { gap: 22px; }
  .card--back .brand__square { width: 110px; height: 110px; border-radius: 10px; }
  .card--back .brand__name { font-size: 56px; color: #161616; }
</style>
</head>
<body>
<main class="stage">
  <section class="card card--front" aria-label="Card front">
    <div class="brand">
      <span class="brand__square"></span>
      <span class="brand__name">Norvane Solutions</span>
    </div>
    <div class="divider"></div>
    <div class="contact">
      <p class="contact__name">Daniel Reyes</p>
      <p class="contact__title">IT Consultant</p>
      <ul class="contact__list">
        <li class="contact__item">
          <svg class="contact__icon" viewBox="0 0 14 14"><path d="M3 1.5l2 .3 1 3-1.5 1a7 7 0 0 0 3.7 3.7l1-1.5 3 1 .3 2c-.5 1-1.5 1.5-2.5 1.5A10 10 0 0 1 1.5 4C1.5 3 2 2 3 1.5z" fill="var(--accent-yellow)"/></svg>
          (555)014-2290
        </li>
        <li class="contact__item">
          <svg class="contact__icon" viewBox="0 0 14 14"><rect x="3.5" y="1" width="7" height="12" rx="1.2" fill="none" stroke="var(--accent-red)" stroke-width="1.5"/><circle cx="7" cy="11" r=".8" fill="var(--accent-red)"/></svg>
          (555) 013-7741
        </li>
        <li class="contact__item">
          <svg class="contact__icon" viewBox="0 0 14 14"><rect x="1" y="3" width="12" height="8.5" fill="var(--accent-sky)"/><path d="M1 3l6 5 6-5" fill="none" stroke="#fff" stroke-width="1"/></svg>
          daniel.reyes@norvane.ca
        </li>
        <li class="contact__item">
          <svg class="contact__icon" viewBox="0 0 14 14"><circle cx="7" cy="7" r="6" fill="var(--accent-navy)"/><ellipse cx="7" cy="7" rx="2.6" ry="6" fill="none" stroke="#fff" stroke-width=".8"/><path d="M1 7h12" stroke="#fff" stroke-width=".8"/></svg>
          www.norvane.ca
        </li>
      </ul>
    </div>
  </section>

  <section class="card card--back" aria-label="Card back">
    <div class="brand">
      <span class="brand__square"></span>
      <span class="brand__name">Norvane Solutions</span>
    </div>
  </section>
</main>
</body>
</html>
```